"Nail Care" Postcard

Hello,

We are looking to redesign our current post card. The target audience of this post card age is 50+. We will be mailing these postcards through Harbor Press.
The goal of the message is to remind them that it is time to get their (toe) nail care done.

Attached is our previous postcard.
Post card size: 4.2” x 5.5”
Backside of the postcards needs space for the mailing address and postage.
Our address and logo need to be present.
The message of the back of the postcard needs to be present as well.
Examples of stock images must come with the example.
Files preferred to be in TIFF or .ai

Thank you,
Marcus T.

```html
<!DOCTYPE html>
<html lang="en">
<head>
<meta charset="utf-8">
<title>Nail Care Postcard</title>
<link href="https://fonts.googleapis.com/css2?family=Poppins:ital,wght@0,400;0,700;0,800;1,700&family=Roboto+Slab:wght@400;700&family=Fira+Sans:wght@500;600&display=swap" rel="stylesheet">
<style>
  :root {
    --stage: #8e8e8e;
    --orange: #f4874f;
    --teal: #3ec4a0;
    --teal-dark: #2e9e82;
    --white: #ffffff;
    --mail-gray: #e0e0e0;
    --ink: #222222;
  }
  * { margin: 0; padding: 0; box-sizing: border-box; }
  html, body { width: 1040px; height: 1200px; overflow: hidden; background: var(--stage); }
  .card {
    position: absolute; left: 237px; width: 578px; height: 441px;
    background: var(--white); box-shadow: 0 2px 4px rgba(0,0,0,.35); overflow: hidden;
  }
  .card--front { top: 131px; }
  .card--back { top: 645px; background: var(--mail-gray); }
  .card svg.shapes { position: absolute; inset: 0; }
  .abs { position: absolute; }

  /* front */
  .headline { left: 20px; width: 240px; top: 128px; text-align: center; font-family: "Poppins", sans-serif; font-weight: 800; line-height: .95; }
  .headline .l1 { color: var(--orange); font-size: 31px; display: block; }
  .headline .l2 { color: var(--orange); font-size: 54px; display: block; line-height: .9; }
  .headline .l3 { color: var(--teal); font-size: 31px; display: block; }
  .brand { font-family: "Poppins", sans-serif; font-weight: 700; color: var(--orange); display: flex; align-items: center; gap: 8px; }
  .brand .dot { width: 36px; height: 36px; border-radius: 50%; background: var(--teal); flex: none; }
  .brand--front { right: 26px; top: 34px; font-size: 19px; }
  .tagline { right: 26px; top: 88px; font-family: "Poppins", sans-serif; font-size: 19px; color: var(--teal); }
  .tagline b { font-style: italic; font-weight: 700; }
  .front-phone { right: 30px; top: 366px; font-family: "Poppins", sans-serif; font-weight: 700; font-size: 29px; color: var(--orange); letter-spacing: .5px; }
  .front-web { right: 31px; top: 397px; font-family: "Poppins", sans-serif; font-weight: 700; font-size: 16px; color: var(--teal); letter-spacing: .5px; }

  /* back */
  .brand--back { left: 31px; top: 22px; font-size: 13px; }
  .brand--back .dot { width: 24px; height: 24px; }
  .return-address { left: 31px; top: 67px; font-family: "Roboto Slab", serif; font-size: 11.5px; line-height: 14.5px; color: var(--ink); }
  .slogan { left: 200px; width: 260px; top: 26px; text-align: center; font-family: "Roboto Slab", serif; font-weight: 700; color: var(--teal-dark); line-height: 1; }
  .slogan .big { display: block; font-size: 43px; }
  .slogan .small { display: block; font-size: 31px; margin-top: 1px; }
  .reminder { left: 10px; width: 276px; top: 172px; text-align: center; font-family: "Fira Sans", sans-serif; color: var(--white); }
  .reminder .lead { font-size: 19px; font-weight: 500; line-height: 22.5px; }
  .reminder .ask { font-size: 14px; font-weight: 500; line-height: 15px; margin-top: 9px; }
  .reminder .phone { font-size: 31px; font-weight: 600; margin-top: 6px; letter-spacing: .5px; }
  .reminder .note { font-size: 8.5px; font-weight: 600; line-height: 11px; margin-top: 6px; }
</style>
</head>
<body>

<section class="card card--front">
  <svg class="shapes" width="578" height="441" viewBox="0 0 578 441">
    <defs>
      <linearGradient id="treatmentTone" x1="0" y1="0" x2="1" y2="1">
        <stop offset="0" stop-color="#cfc6bf"/>
        <stop offset=".5" stop-color="#e6d2c4"/>
        <stop offset="1" stop-color="#d9d6d3"/>
      </linearGradient>
      <radialGradient id="feetTone" cx=".5" cy=".5" r=".6">
        <stop offset="0" stop-color="#e7bba6"/>
        <stop offset="1" stop-color="#f3eeee"/>
      </radialGradient>
    </defs>
    <path d="M238 0 C290 60 335 115 360 170" fill="none" stroke="var(--orange)" stroke-width="6"/>
    <path d="M360 320 C330 375 300 410 250 441" fill="none" stroke="var(--teal)" stroke-width="8"/>
    <path role="img" aria-label="Photo of a gloved specialist trimming a patient's toenails"
          d="M0 0 H232 C290 60 335 115 352 165 A116 116 0 0 0 354 322 C322 378 290 410 243 441 H0 Z"
          fill="url(#treatmentTone)"/>
    <circle role="img" aria-label="Photo of a pair of bare feet with a discoloured toenail"
            cx="452" cy="247" r="113" fill="url(#feetTone)"/>
  </svg>
  <h1 class="abs headline"><span class="l1">HAVE YOUR</span><span class="l2">NAILS</span><span class="l3">BEEN TAKEN<br>CARE OF?</span></h1>
  <div class="abs brand brand--front"><span class="dot"></span><span>LINDEN FOOT &amp; ANKLE</span></div>
  <p class="abs tagline">We Keep <b>You Moving</b></p>
  <p class="abs front-phone">877-555-0142</p>
  <p class="abs front-web">WWW.STEADYSTEPFEET.COM</p>
</section>

<section class="card card--back">
  <svg class="shapes" width="578" height="441" viewBox="0 0 578 441">
    <rect x="0" y="0" width="450" height="137" fill="var(--white)"/>
    <rect x="0" y="0" width="292" height="200" fill="var(--white)"/>
    <path d="M0 178 L150 121 C195 104 245 106 278 124" fill="none" stroke="var(--teal-dark)" stroke-width="7"/>
    <path d="M0 186 L150 129 C205 108 262 114 292 140 V367 H70 V441 H0 Z" fill="var(--orange)"/>
  </svg>
  <div class="abs brand brand--back"><span class="dot"></span><span>LINDEN FOOT &amp; ANKLE</span></div>
  <address class="abs return-address" style="font-style:normal">58 Orchard Hill Rd.<br>Ste. 210<br>Linden, MD 21900</address>
  <h2 class="abs slogan"><span class="big">WE KEEP</span><span class="small">YOU MOVING</span></h2>
  <div class="abs reminder">
    <p class="lead">We are pleased to<br>inform you may be due for<br>your bimonthly nail care!</p>
    <p class="ask">Please call our office to<br>schedule your appointment.</p>
    <p class="phone">(877)555-0142</p>
    <p class="note">*If you have received nail card within the past<br>two months, please disregard*</p>
  </div>
</section>

</body>
</html>
```